Brovanta Energy Ratings Whole Home Energy Rating Flyer

Please create a flyer 8.5" x 11" that is 2-sided that goes hand and hand with my tri-fold flyer. The flyer will target prospective homeowners and real estate agents to purchase a whole home energy rating. I have attached further details.

Target Market(s)

Homeowners looking to remodel their homes, save on energy bills, purchase or sell a home.

Font styles to use
Serif
Sans Serif

Colors
3176b5
ffffff

Requirements
Must have
• Must be able to sell a whole home energy rating on its own!
Nice to have
• I would like to mimic the colors and background of my tri-fold flyer.
Should not have
• Should not be boring!

```html
<!DOCTYPE html>
<html lang="en">
<head>
<meta charset="utf-8">
<title>Brovanta Energy Ratings – Whole Home Energy Rating Flyer</title>
<link rel="stylesheet" href="https://fonts.googleapis.com/css2?family=Roboto:ital,wght@0,400;0,500;0,700;1,700&family=Roboto+Condensed:wght@500;700&display=swap">
<style>
:root{
  --brand-blue:#3176b5;
  --bright-blue:#1e8ce6;
  --ink:#1c1c1c;
  --black:#050505;
  --stage:#404040;
  --panel-grey:#e6e6e6;
  --white:#ffffff;
}
*{box-sizing:border-box;margin:0;padding:0}
html,body{width:1200px;height:1200px;overflow:hidden;background:var(--stage)}
body{position:relative;font-family:"Roboto",Arial,sans-serif;color:var(--ink)}
.sheet{position:absolute;top:235px;width:540px;height:693px;background:linear-gradient(180deg,#fafafa,#eef0f2);overflow:hidden;box-shadow:0 4px 14px rgba(0,0,0,.45)}
.sheet--front{left:43px}
.sheet--back{left:616px}
.sheet-label{position:absolute;top:970px;width:540px;text-align:center;color:var(--white);font:700 50px/1 "Roboto",Arial,sans-serif}
.abs{position:absolute}
.photo{position:absolute;left:0;top:0;width:100%}
.house-photo{height:265px;background:linear-gradient(180deg,#b9cfe6 0%,#d9d6d2 40%,#8b8580 70%,#6b6a4f 100%)}
.solar-photo{height:243px;background:linear-gradient(180deg,#3f73c6 0%,#7aa3dc 35%,#55627a 60%,#cfd9ec 100%)}
.deco{position:absolute;left:0;top:0}
.brand{position:absolute;left:345px;top:34px;width:180px;text-align:right}
.brand-name{display:flex;align-items:center;justify-content:flex-end;gap:6px;font:700 27px/1 "Roboto",Arial,sans-serif;color:var(--ink);letter-spacing:.5px}
.brand-name .mark{width:12px;height:12px;background:var(--brand-blue)}
.brand-tag{font:500 8px/1 "Roboto",Arial,sans-serif;color:var(--brand-blue);letter-spacing:.6px;margin-top:3px}
.intro{position:absolute;left:18px;top:275px;width:470px;color:var(--white);font:500 13px/16px "Roboto Condensed",Arial,sans-serif}
.section-title{position:absolute;left:16px;padding-left:9px;border-left:3px solid var(--brand-blue);font:italic 700 15.5px/20px "Roboto",Arial,sans-serif;color:var(--brand-blue)}
.copy{position:absolute;left:16px;width:506px;font-size:9.8px;line-height:12.3px;text-align:justify}
.copy p+p{margin-top:9px}
.footer{position:absolute;left:0;bottom:0;width:100%;height:38px;background:var(--black);display:flex;align-items:center;justify-content:center;gap:8px;color:var(--bright-blue);font:700 15px/1 "Roboto",Arial,sans-serif}
.footer .phone{display:flex;align-items:center;gap:6px;font-size:14px}
.web-tab{position:absolute;right:0;top:18px;width:142px;height:26px;background:var(--black);color:var(--white);font:700 9.5px/26px "Roboto",Arial,sans-serif;text-align:center}
.checklist{position:absolute;left:20px;top:344px;width:505px;display:grid;grid-template-columns:117px 165px 113px 110px;row-gap:10px;list-style:none;font-size:9.6px;line-height:11px}
.checklist li{display:flex;gap:3px;align-items:flex-start;min-height:16px}
.checklist svg{flex:none;margin-top:1px}
.facts{position:absolute;left:0;top:427px;width:100%;height:130px;background:var(--panel-grey);padding:10px 18px 0 22px;list-style:none;font-size:7.6px;line-height:9.6px}
.facts li{position:relative;margin-bottom:5.5px}
.facts li::before{content:"•";position:absolute;left:-6px}
.review-by{text-align:right;padding-right:60px;margin-top:2px;font-size:11px}
</style>
</head>
<body>

<!-- Front side -->
<section class="sheet sheet--front">
  <div class="photo house-photo" role="img" aria-label="Photo of a large two-storey shingled family home lit warmly at dusk with a garage and front porch"></div>
  <svg class="deco" width="540" height="693" viewBox="0 0 540 693" aria-hidden="true">
    <polygon points="0,265 540,265 540,282 460,330 0,330" fill="#3176b5" fill-opacity=".9"/>
    <polygon points="540,282 540,290 475,330 460,330" fill="#050505"/>
    <polygon points="460,330 475,330 462,336 0,336 0,330" fill="#050505"/>
    <polygon points="540,610 540,655 465,655" fill="#050505"/>
  </svg>
  <div class="brand">
    <div class="brand-name"><span class="mark"></span>BROVANTA</div>
    <div class="brand-tag">ENERGY RATINGS</div>
  </div>
  <p class="intro">Would you like to lower your monthly energy bill, enjoy a safer, more comfortable and durable home, and increase your homes appraisal value and sales appeal? Then keep reading, because that is what a lost cost, home energy rating can do for you…</p>

  <h2 class="section-title" style="top:344px">What is a Whole Home Energy Rating?</h2>
  <div class="copy" style="top:372px">
    <p>A Whole Home Energy Rating is a comprehensive evaluation of the efficiency of the entire home. You will receive a written report that includes a numeric score or “rating” of the home, plus recommendations for improvements that will reduce energy bills and make the home more comfortable. Each rating will receive an official California Home Energy Rating Certificate and home energy rating report with the California Energy Commission’s (CEC) seal. The report will identify the most cost-effective and appropriate energy efficiency improvements needed to save you money and provide long lasting comfort.</p>
  </div>

  <h2 class="section-title" style="top:455px">Who needs a Whole Home Energy Rating?</h2>
  <div class="copy" style="top:482px">
    <p>Everyone! Whether you are buying or selling, or plan on staying in your home for one year or the rest of your life, each whole home energy rating is geared toward helping you save money, and is custom tailored to fit your unique needs. The whole home energy rating can be designed to fit any lifestyle or energy improvement budget, with a focal point on cost effectiveness and common sense.</p>
    <p>Buyers who choose to get a whole home energy rating can better decide which home will save them money through energy efficiency! They may also be entitled to federal tax credits, and borrow up to $40,000 for energy improvements through their mortgage.</p>
    <p>Sellers who have a CEC certificate showing their homes energy efficiency ultimately make their homes more valuable and often sell their homes faster than those without documentation.</p>
    <p style="width:450px">Before you remodel your home, make sure you have a HERS Rater conduct a Whole Home Energy Rating so you know exactly where to focus your money.</p>
  </div>

  <div class="footer">
    <span>Call Today !</span>
    <span class="phone">
      <svg width="17" height="17" viewBox="0 0 20 20" aria-hidden="true"><circle cx="10" cy="10" r="8.6" fill="none" stroke="#d0d0d0" stroke-width="1.4"/><path d="M7 5.5l1.6 2.3-1 1.2c.6 1.3 1.5 2.2 2.8 2.8l1.2-1 2.3 1.6-.9 1.6c-3.4-.4-6.1-3.1-6.6-6.6z" fill="#d0d0d0"/></svg>
      (555) 014 - 2760
    </span>
  </div>
</section>

<!-- Back side -->
<section class="sheet sheet--back">
  <div class="photo solar-photo" role="img" aria-label="Photo of two technicians in hard hats installing solar panels on a roof under a blue sky"></div>
  <svg class="deco" width="540" height="693" viewBox="0 0 540 693" aria-hidden="true">
    <polygon points="0,243 540,200 540,243" fill="#fafafa"/>
    <polygon points="0,236 540,196 540,204 0,243" fill="#050505"/>
    <polygon points="540,614 540,656 470,656" fill="#050505"/>
  </svg>
  <div class="web-tab">www.brovantaratings.com</div>

  <h2 class="section-title" style="top:255px">Who performs the rating?</h2>
  <div class="copy" style="top:282px;left:21px;width:503px">
    <p>A Home Energy Rating System (HERS) Rater, who is certified by the CEC will conduct the rating. Each California HERS Rater must follow standardized energy auditing procedures and use energy analysis software that meets CEC requirements.</p>
    <p style="margin-top:4px;text-align:left">The HERS Rater will inspect and assess all the major energy efficiency features of your home:</p>
  </div>

  <ul class="checklist">
    <li><svg width="10" height="10" viewBox="0 0 10 10" aria-hidden="true"><path d="M1 5.5l2.5 3L9 1" fill="none" stroke="#3176b5" stroke-width="1.8"/></svg>Air leaks</li>
    <li><svg width="10" height="10" viewBox="0 0 10 10" aria-hidden="true"><path d="M1 5.5l2.5 3L9 1" fill="none" stroke="#3176b5" stroke-width="1.8"/></svg>Cooling system</li>
    <li><svg width="10" height="10" viewBox="0 0 10 10" aria-hidden="true"><path d="M1 5.5l2.5 3L9 1" fill="none" stroke="#3176b5" stroke-width="1.8"/></svg>Heating system</li>
    <li><svg width="10" height="10" viewBox="0 0 10 10" aria-hidden="true"><path d="M1 5.5l2.5 3L9 1" fill="none" stroke="#3176b5" stroke-width="1.8"/></svg>Cooling/heating duct system</li>
    <li><svg width="10" height="10" viewBox="0 0 10 10" aria-hidden="true"><path d="M1 5.5l2.5 3L9 1" fill="none" stroke="#3176b5" stroke-width="1.8"/></svg>Water heating system</li>
    <li><svg width="10" height="10" viewBox="0 0 10 10" aria-hidden="true"><path d="M1 5.5l2.5 3L9 1" fill="none" stroke="#3176b5" stroke-width="1.8"/></svg>Insulation (attic,walls,floor,roof)</li>
    <li><svg width="10" height="10" viewBox="0 0 10 10" aria-hidden="true"><path d="M1 5.5l2.5 3L9 1" fill="none" stroke="#3176b5" stroke-width="1.8"/></svg>Windows</li>
    <li><svg width="10" height="10" viewBox="0 0 10 10" aria-hidden="true"><path d="M1 5.5l2.5 3L9 1" fill="none" stroke="#3176b5" stroke-width="1.8"/></svg>Lighting</li>
    <li><svg width="10" height="10" viewBox="0 0 10 10" aria-hidden="true"><path d="M1 5.5l2.5 3L9 1" fill="none" stroke="#3176b5" stroke-width="1.8"/></svg>Major appliances</li>
    <li><svg width="10" height="10" viewBox="0 0 10 10" aria-hidden="true"><path d="M1 5.5l2.5 3L9 1" fill="none" stroke="#3176b5" stroke-width="1.8"/></svg>Solar (if any)</li>
    <li><svg width="10" height="10" viewBox="0 0 10 10" aria-hidden="true"><path d="M1 5.5l2.5 3L9 1" fill="none" stroke="#3176b5" stroke-width="1.8"/></svg>Other energy uses</li>
    <li><svg width="10" height="10" viewBox="0 0 10 10" aria-hidden="true"><path d="M1 5.5l2.5 3L9 1" fill="none" stroke="#3176b5" stroke-width="1.8"/></svg>Prior energy bills</li>
  </ul>

  <ul class="facts">
    <li>Every report is custom tailored to each unique home.</li>
    <li>Brovanta Energy Ratings includes a free duct leakage test and free building envelope leakage test with each home energy audit.</li>
    <li>Heating and cooling ducts in an average California home leak almost 30 percent. That is why when heating or cooling equipment is replaced, testing the system’s ducts for leaks is now required by building officials in many parts of the state.</li>
    <li>You wouldn’t buy a new car without knowing the “miles per gallon”, so why buy a home without knowing the “home energy rating?”</li>
    <li>After your mortgage payment, your energy bill is often the second largest monthly home ownership expense.</li>
    <li>Combine an Energy Efficient Mortgage (EEM) with other programs and you may be able to borrow up to $40,000 or more for efficiency improvements. Ask a knowledgeable lender if an EEM is right for you.</li>
  </ul>

  <h2 class="section-title" style="top:563px">Customer Reviews :</h2>
  <div class="copy" style="top:592px;left:21px;width:508px;font-size:10px">
    <p style="text-align:left">While having my air conditioning replaced, my ac contractor called this company to do the duct test. Mr. Halden arrived right on time, and explained the process thoroughly. He was clean and efficient while working throughout the house. He put my mind at ease during the process. I would definitely recommend this company.</p>
    <p class="review-by">– Dana R.</p>
  </div>

  <div class="footer">
    <span>Call Today !</span>
    <span class="phone">
      <svg width="17" height="17" viewBox="0 0 20 20" aria-hidden="true"><circle cx="10" cy="10" r="8.6" fill="none" stroke="#d0d0d0" stroke-width="1.4"/><path d="M7 5.5l1.6 2.3-1 1.2c.6 1.3 1.5 2.2 2.8 2.8l1.2-1 2.3 1.6-.9 1.6c-3.4-.4-6.1-3.1-6.6-6.6z" fill="#d0d0d0"/></svg>
      (555) 014 - 2760
    </span>
  </div>
</section>

<div class="sheet-label" style="left:37px">Front</div>
<div class="sheet-label" style="left:616px">Back</div>

</body>
</html>
```